Brambleton Resource Holdings, LP Letter Head

We need an official company letter head design that is clean and mimics our company logo style. It will include our logo, address, phone, and website. We are an OIl and Gas mineral purchasing company, so hints of oil rigs or related design would be desirable.

Industry/Entity Type

Oil And Gas

Colors
ec1f27
f04a50
f59195
fbd4d5

Requirements
Must have
• Logo
• 7392 Whitcombe R. Ashdale Parkway, Suite 618
• Dallas TX, 75391
• 214-673-1958
• www.bramblestoneres.example
Nice to have
• Oil Rigs or OIl and gas related design

```html
<!DOCTYPE html>
<html lang="en">
<head>
<meta charset="utf-8">
<title>Brambleton Resource Holdings, LP – Letterhead and Folder</title>
<link href="https://fonts.googleapis.com/css2?family=Questrial&display=swap" rel="stylesheet">
<style>
  :root {
    --red: #ec1f27;
    --red-mid: #f04a50;
    --red-soft: #f59195;
    --red-pale: #fbd4d5;
    --ink: #3a3a3a;
    --grey: #bdbdbd;
    --rig: #d9d9d9;
    --stage: #e6e6e6;
    --paper: #ffffff;
    --folder: #f0f0f0;
  }
  * { margin: 0; padding: 0; box-sizing: border-box; }
  html, body { width: 1200px; height: 894px; overflow: hidden; }
  body { background: var(--stage); font-family: "Questrial", sans-serif; color: var(--ink); position: relative; }

  /* Letterhead sheet */
  .letterhead {
    position: absolute; left: 74px; top: 73px;
    width: 521px; height: 674px;
    background: var(--paper); overflow: hidden;
    box-shadow: 0 6px 14px rgba(0,0,0,0.14);
  }
  .brand { position: absolute; left: 54px; top: 26px; width: 148px; text-align: center; }
  .brand-square { width: 60px; height: 60px; background: var(--red); margin: 0 auto 6px; }
  .brand-name { color: var(--red); font-size: 14px; line-height: 16px; }

  .header-rule { position: absolute; left: 209px; top: 100px; width: 270px; height: 1px; background: var(--ink); }
  .contact { position: absolute; right: 44px; top: 70px; font-size: 7.5px; line-height: 12px; }
  .phone { display: flex; justify-content: flex-end; align-items: center; gap: 4px; }
  .phone svg { width: 8px; height: 8px; }
  .address { position: absolute; right: 44px; top: 106px; text-align: right; color: var(--red); font-size: 7px; line-height: 11px; font-weight: bold; font-style: normal; }

  .watermark { position: absolute; left: 129px; top: 219px; width: 239px; height: 236px; background: var(--red-pale); opacity: 0.55; }
  .rig-illustration { position: absolute; left: 182px; top: 479px; width: 339px; height: 195px;
    background: linear-gradient(to bottom, rgba(217,217,217,0) 0%, var(--rig) 40%, #d0d0d0 100%); }

  .body-copy { position: absolute; left: 55px; top: 157px; width: 411px; font-size: 10.4px; line-height: 17.1px; text-align: justify; hyphens: auto; }
  .body-copy p { margin-bottom: 17.1px; }

  .signature { position: absolute; left: 380px; top: 585px; }
  .signature-name { font-size: 13.5px; }
  .signature-title { font-size: 9px; margin-top: 6px; }

  .footer-brand { position: absolute; left: 48px; top: 556px; width: 117px; text-align: center; }
  .footer-square { width: 47px; height: 47px; background: var(--grey); opacity: 0.6; margin: 0 auto 6px; }
  .footer-name { color: var(--grey); font-size: 9.5px; line-height: 11px; }

  .footer-rule { position: absolute; left: 46px; top: 644px; width: 430px; height: 1px; background: var(--ink); }
  .website { position: absolute; left: 0; width: 521px; top: 652px; text-align: center; color: var(--red); font-size: 9px; letter-spacing: 2.7px; font-weight: bold; }

  /* Folder cover */
  .folder-cover {
    position: absolute; left: 638px; top: 72px;
    width: 498px; height: 676px;
    background: var(--folder); border-radius: 14px;
    box-shadow: 0 6px 14px rgba(0,0,0,0.12);
  }
  .cover-brand { position: absolute; left: 0; width: 498px; top: 453px; text-align: center; }
  .cover-square { width: 103px; height: 103px; background: var(--red); margin: 0 auto 16px; }
  .cover-name { color: var(--red); font-size: 26px; line-height: 29px; }
</style>
</head>
<body>
<main class="letterhead">
  <div class="watermark" aria-hidden="true"></div>
  <div class="rig-illustration" role="img" aria-label="Grey silhouette of an offshore oil rig platform with cranes and a drilling derrick"></div>

  <header>
    <div class="brand">
      <div class="brand-square" aria-hidden="true"></div>
      <div class="brand-name">Brambleton Resource<br>Holdings, LP</div>
    </div>
    <div class="header-rule"></div>
    <div class="contact">
      <div class="phone">214-673-1958
        <svg viewBox="0 0 10 10"><circle cx="5" cy="5" r="5" fill="var(--red)"/><path d="M3 3.2c.3-.4.8-.4 1 0l.4.7-.5.5c.3.7.8 1.2 1.5 1.5l.5-.5.7.4c.4.2.4.7 0 1-1.8.6-4.2-1.8-3.6-3.6z" fill="#fff"/></svg>
      </div>
      <div class="phone">214-508-3361
        <svg viewBox="0 0 10 10"><circle cx="5" cy="5" r="5" fill="var(--red)"/><rect x="2.8" y="3.2" width="4.4" height="3.6" rx="0.6" fill="#fff"/></svg>
      </div>
    </div>
    <address class="address">7392 Whitcombe R. Ashdale Parkway<br>Suite 618, Dallas TX, 75391</address>
  </header>

  <section class="body-copy">
    <p>Lorem ipsum dolor sit amet, consectetur adipiscing elit. Donec orci purus, luctus vitae dignissim eu, iaculis sed purus. Vivamus faucibus, ipsum nec aliquet viverra, leo mauris condimentum ligula, sit amet sagittis enim ligula quis arcu. Nam egestas tortor id nisi porttitor mattis. In tortor ante, ultricies in suscipit a, tempus non massa. Vivamus et auctor mi. Fusce vel massa nulla. Phasellus nec eros mauris, et scelerisque orci. Donec malesuada orci vitae nulla accumsan porta a id massa.</p>
    <p>Quisque accumsan iaculis magna sit amet fringilla. Maecenas consequat, magna eget tincidunt semper, odio nibh rutrum mi, id feugiat ante nisi eu risus. Vestibulum nunc orci, rhoncus a placerat in, ultricies in mi. Cras mattis varius eros, vel fringilla nisi suscipit eget. Quisque scelerisque sagittis nulla at porttitor. Mauris a justo et tellus interdum tristique. Sed id augue vitae urna euismod commodo aliquet a quam. Pellentesque arcu velit, cursus et malesuada ut, consequat et diam. Nullam erat sem, rhoncus id ullamcorper vitae, rhoncus et arcu. In ultricies ultricies nulla,</p>
    <p>Kut rutrum nisi iaculis at. Donec eu magna a metus ornare faucibus. Fusce aliquet faucibus ultricies. Morbi semper, est id tincidunt gravida, sem arcu adipiscing lacus, ac bibendum nulla leo eu purus. Quisque nec diam sed risus consectetur a ccumsan quis quis nibh. Vestibulum id purus lorem. Donec eu magna a metus ornare faucibus. Fusce aliquet faucibus ultricies. Morbi semper, est id tincidunt gravida, sem arcu adipiscing lacus, ac bibendum nulla leo eu purus. Quisque nec diam sed risus consectetur a ccumsan quis quis nibh. Vestibulum id purus lorem.</p>
  </section>

  <div class="signature">
    <div class="signature-name">Dana Whitlow</div>
    <div class="signature-title">Co-Founder &amp; CEO</div>
  </div>

  <footer>
    <div class="footer-brand">
      <div class="footer-square" aria-hidden="true"></div>
      <div class="footer-name">Brambleton Resource<br>Holdings, LP</div>
    </div>
    <div class="footer-rule"></div>
    <div class="website">www.bramblestoneres.example</div>
  </footer>
</main>

<aside class="folder-cover">
  <div class="cover-brand">
    <div class="cover-square" aria-hidden="true"></div>
    <div class="cover-name">Brambleton Resource<br>Holdings, LP</div>
  </div>
</aside>
</body>
</html>
```